Lumo Care — Premium Telehealth Marketing Website

Lumo Care is a modern, cash-pay telehealth brand offering prescription weight-loss (GLP-1) and sexual-health treatment online, with licensed US providers — no insurance required. We're building a premium, trustworthy direct-to-consumer healthcare brand in the same tier as Welk, Tu, and Orla.

We need a clean, modern, premium marketing website design — warm and trustworthy, not cold or clinical. Think high-end wellness brand: generous whitespace, elegant typography, calm and confident. It should feel medically credible but human and approachable.

WHAT WE NEED DESIGNED (3 core templates that define the whole site):

1. Homepage — the brand showcase that establishes the full visual language (hero, sections, product highlights, how-it-works, trust elements, footer).

2. Product / Treatment page template — a reusable layout for any medication (transparent pricing, how it works, what's included, clinical info, safety, clear call-to-action). We'll reuse this pattern for all treatments.

3. Interior / Content page template — a flexible layout for sub-pages like How It Works, About, Contact, FAQ, and legal pages.

We'll implement the final site ourselves in React/Next.js + Tailwind CSS, so clean, well-structured design (and HTML/CSS if you provide it) is a strong plus.

BRAND DIRECTION (already established — please design within this):

- Logo: lowercase wordmark "lumo." with the period in gold (see attached). Please build the design around this existing logo.
- Colors: deep navy (#0B1B33 and #14315C) with a warm gold accent (#E0A458); soft light backgrounds (#EEF3F9, #FBFCFE).
- Typography: a refined serif for headlines (e.g., Fraunces) paired with a clean sans-serif for body (e.g., Inter).
- Tone: premium, warm, trustworthy, human.

INSPIRATION / QUALITY BAR: Welk (welk.example), Tu (tu.example), Orla — the polished DTC healthcare aesthetic. We want that tier of quality, with our own warmer navy-and-gold identity.

Industry/Entity Type

Telemedicine

Coding

Coded - Design and coding required

Number of Pages Required

3 page

Requirements
Nice to have
• Side Scrolling Medictions bar like on Tu.example

```html
<!DOCTYPE html>
<html lang="en">
<head>
<meta charset="utf-8">
<title>Sildenafil &amp; Tadalafil — Prescribing &amp; Important Safety Information | Lumo Care</title>
<link href="https://fonts.googleapis.com/css2?family=Cormorant+Garamond:wght@500;600&family=Figtree:wght@400;500;600;700&display=swap" rel="stylesheet">
<style>
  :root {
    --bg: #0b1628;
    --bg-warning: #1c1a29;
    --text: #c6ceda;
    --text-muted: #8a96a8;
    --heading: #f1f3f7;
    --accent: #1fb1d4;
    --accent-button: #18809a;
    --danger: #ff5f5f;
    --danger-text: #ff6b6b;
    --rule: #1c2a40;
    --border: #3a4558;
  }
  * { box-sizing: border-box; margin: 0; padding: 0; }
  html, body { width: 1200px; height: 2241px; overflow: hidden; }
  body {
    background: var(--bg);
    color: var(--text);
    font-family: "Figtree", sans-serif;
    font-size: 13.3px;
    line-height: 22.5px;
    position: relative;
  }

  /* Header */
  .site-header { height: 62px; position: relative; }
  .brand {
    position: absolute;
    left: 24px;
    top: 18px;
    font-weight: 600;
    font-size: 17px;
    color: var(--heading);
    line-height: 26px;
  }
  .main-nav {
    position: absolute;
    top: 21px;
    left: 370px;
    display: flex;
    gap: 36px;
    font-size: 11.8px;
    font-weight: 500;
    color: #b8c2d0;
  }
  .main-nav a { color: inherit; text-decoration: none; }
  .header-actions {
    position: absolute;
    top: 11px;
    right: 25px;
    display: flex;
    gap: 10px;
  }
  .btn {
    height: 40px;
    border-radius: 6px;
    font-size: 11.8px;
    font-weight: 600;
    display: flex;
    align-items: center;
    justify-content: center;
    color: #fff;
    text-decoration: none;
  }
  .btn-outline { width: 87px; border: 1px solid var(--border); }
  .btn-primary { width: 107px; background: var(--accent-button); }

  /* Content */
  .doc { width: 627px; margin: 0 auto; padding-top: 38px; }
  .doc-title {
    font-family: "Cormorant Garamond", serif;
    font-weight: 500;
    font-size: 38px;
    line-height: 46px;
    color: var(--heading);
  }
  .doc-kicker {
    margin-top: 10px;
    font-size: 12px;
    font-weight: 600;
    letter-spacing: 0.06em;
    color: var(--accent);
    line-height: 16px;
  }
  .doc-rule { margin-top: 21px; height: 2px; background: var(--accent); }

  .boxed-warning {
    margin-top: 34px;
    background: var(--bg-warning);
    border: 1px solid #2d2636;
    border-left: 3px solid var(--danger);
    border-radius: 5px;
    padding: 19px 18px 18px 18px;
    color: var(--danger-text);
    font-size: 12.9px;
    line-height: 21.6px;
  }
  .boxed-warning h2 {
    font-size: 13.8px;
    font-weight: 700;
    line-height: 18px;
    margin-bottom: 9px;
    color: var(--danger);
  }
  .boxed-warning p + p { margin-top: 21px; }

  .section { margin-top: 28px; }
  .section h2 {
    font-family: "Cormorant Garamond", serif;
    font-weight: 500;
    font-size: 22px;
    line-height: 30px;
    color: var(--heading);
    padding-bottom: 6px;
    border-bottom: 1px solid var(--rule);
    margin-bottom: 17px;
  }
  .section ul { list-style: none; }
  .section li { position: relative; padding-left: 20px; }
  .section li::before {
    content: "";
    position: absolute;
    left: 6px;
    top: 10px;
    width: 4px;
    height: 4px;
    border-radius: 50%;
    background: var(--text);
  }
  .section li strong { color: #e6eaf0; font-weight: 700; }

  .list-spaced li + li { margin-top: 8px; }
  .section p + .list-spaced { margin-top: 13px; }
  .list-spaced + p { margin-top: 15px; }

  .precaution h3 {
    font-size: 14px;
    font-weight: 700;
    letter-spacing: 0.05em;
    color: var(--accent);
    line-height: 20px;
    margin-bottom: 6px;
  }
  .precaution + .precaution { margin-top: 15px; }

  /* Footer */
  .site-footer {
    position: absolute;
    left: 0;
    top: 1910px;
    width: 1200px;
    height: 331px;
    border-top: 1px solid #15223a;
  }
  .footer-brand {
    position: absolute;
    left: 84px;
    top: 78px;
    font-weight: 600;
    font-size: 16px;
    color: var(--heading);
    line-height: 24px;
  }
  .footer-tagline {
    position: absolute;
    left: 84px;
    top: 128px;
    width: 240px;
    font-size: 11.4px;
    line-height: 20px;
    color: var(--text-muted);
  }
  .footer-col { position: absolute; top: 79px; }
  .footer-col h4 {
    font-size: 9.6px;
    font-weight: 700;
    letter-spacing: 0.14em;
    color: var(--text-muted);
    line-height: 14px;
    margin-bottom: 16px;
  }
  .footer-col a {
    display: block;
    font-size: 11.8px;
    line-height: 16px;
    color: #a5b0c0;
    text-decoration: none;
  }
  .footer-col a + a { margin-top: 15px; }
  .col-treatments { left: 441px; }
  .col-company { left: 682px; }
  .footer-divider {
    position: absolute;
    left: 84px;
    top: 248px;
    width: 1032px;
    height: 1px;
    background: #15223a;
  }
  .copyright {
    position: absolute;
    left: 84px;
    top: 286px;
    font-size: 9.6px;
    color: #6c788a;
    line-height: 14px;
  }
</style>
</head>
<body>
  <header class="site-header">
    <a class="brand">lumo.</a>
    <nav class="main-nav">
      <a href="#">Products</a>
      <a href="#">How It Works</a>
      <a href="#">FAQ</a>
      <a href="#">About Us</a>
    </nav>
    <div class="header-actions">
      <a class="btn btn-outline" href="#">Support</a>
      <a class="btn btn-primary" href="#">Get Started</a>
    </div>
  </header>

  <main class="doc">
    <h1 class="doc-title">Sildenafil &amp; Tadalafil</h1>
    <p class="doc-kicker">PRESCRIBING &amp; IMPORTANT SAFETY INFORMATION</p>
    <div class="doc-rule"></div>

    <aside class="boxed-warning">
      <h2>WARNING: CARDIOVASCULAR RISK &amp; NITRATES CONTRAINDICATION</h2>
      <p>Do not take Sildenafil (Vireta® active) or Tadalafil (Calistra® active) if you take prescription medications called nitrates (such as nitroglycerin) for chest pain, or if you use recreational drugs called "poppers" (like amyl nitrite).</p>
      <p>Taking these medications together can cause an unsafe, sudden drop in blood pressure. Discuss your cardiovascular health honestly with your medical provider before beginning erectile dysfunction treatment.</p>
    </aside>

    <section class="section">
      <h2>Prescribing Information</h2>
      <p>Sildenafil and Tadalafil are prescription phosphodiesterase type 5 (PDE5) inhibitors indicated for the treatment of erectile dysfunction (ED) in male patients. PDE5 inhibitors work by relaxing smooth muscle tissues and increasing blood flow to specific areas during sexual stimulation.</p>
      <ul class="list-spaced">
        <li><strong>Sildenafil (On-Demand):</strong> Typically taken with water 30 to 60 minutes before planned sexual activity. Its clinical effects last up to 4–6 hours.</li>
        <li><strong>Tadalafil (On-Demand or Daily):</strong> Tadalafil daily (2.5mg–5mg) is taken at the same time each day to support spontaneous erections. On-demand tadalafil is taken before intimacy and remains active in the body for up to 36 hours.</li>
      </ul>
    </section>

    <section class="section" style="margin-top:34px">
      <h2>Common Side Effects</h2>
      <p>The most common side effects of PDE5 inhibitor treatments include:</p>
      <ul class="list-spaced">
        <li>Headache</li>
        <li>Flushing (warmth, redness in the face or neck)</li>
        <li>Dyspepsia (indigestion or upset stomach)</li>
        <li>Nasal congestion or runny nose</li>
        <li>Back pain and muscle aches (more commonly reported with Tadalafil)</li>
        <li>Mild, temporary changes in vision (e.g., color tint, blurred vision)</li>
      </ul>
      <p>Most side effects are mild and resolve on their own within a few hours. If side effects persist or cause distress, contact your prescribing medical provider.</p>
    </section>

    <section class="section" style="margin-top:38px">
      <h2>Limitations of Use</h2>
      <ul class="list-spaced">
        <li>These treatments do not cure erectile dysfunction, increase a man's sexual desire, or prevent pregnancy or the spread of sexually transmitted infections (STIs).</li>
        <li>Do not take PDE5 inhibitors in combination with other treatments for erectile dysfunction.</li>
        <li>These medications are not indicated for use in female patients or pediatric patients.</li>
      </ul>
    </section>

    <section class="section" style="margin-top:36px">
      <h2>Warnings and Precautions</h2>
      <div class="precaution">
        <h3>1. CARDIOVASCULAR RISKS</h3>
        <p>There is a degree of cardiac risk associated with sexual activity. Therefore, physicians should consider the cardiovascular status of patients prior to initiating treatments. PDE5 inhibitors have systemic vasodilatory properties that may result in transient decreases in blood pressure.</p>
      </div>
      <div class="precaution">
        <h3>2. PRIAPISM (PROLONGED ERECTIONS)</h3>
        <p>Erections lasting more than 4 hours (priapism) require immediate emergency medical attention. If priapism is not treated immediately, penile tissue damage and permanent loss of potency could result.</p>
      </div>
      <div class="precaution">
        <h3>3. SUDDEN HEARING LOSS</h3>
        <p>Sudden decrease or loss of hearing, which may be accompanied by tinnitus and dizziness, has been reported. Discontinue medication and seek immediate medical attention if hearing changes occur.</p>
      </div>
      <div class="precaution">
        <h3>4. ALPHA-BLOCKERS AND ANTIHYPERTENSIVES</h3>
        <p>Caution is advised when PDE5 inhibitors are co-administered with alpha-blockers or other antihypertensive agents, as concomitant use can lead to symptomatic hypotension (low blood pressure).</p>
      </div>
      <div class="precaution">
        <h3>5. RENAL AND HEPATIC IMPAIRMENT</h3>
        <p>Dosage adjustments may be necessary for patients with significant renal (kidney) or hepatic (liver) impairment. Discuss all prior diagnoses with your consulting provider.</p>
      </div>
    </section>
  </main>

  <footer class="site-footer">
    <div class="footer-brand">lumo.</div>
    <p class="footer-tagline">Premium online telehealth providing doctor-prescribed treatments without the hassle of traditional clinics.</p>
    <div class="footer-col col-treatments">
      <h4>TREATMENTS</h4>
      <a href="#">Weight Loss (GLP-1)</a>
      <a href="#">Sexual Health Care</a>
    </div>
    <div class="footer-col col-company">
      <h4>COMPANY</h4>
      <a href="#">About Us</a>
      <a href="#">How It Works</a>
    </div>
    <div class="footer-divider"></div>
    <p class="copyright">© 2026 Lumo Care Inc. All rights reserved.</p>
  </footer>
</body>
</html>
```